Quellmark Exteriors Needs a New Website!

We are an exteriors company specializing in vinyl siding, Morten Calloway siding, aluminum soffit/fascia, trough. We do new construction work as well as renovations. We also build detached garages.
You can view our current website at www.quellmarkbuilders.ca
I want to completely overhaul the website.
Our services are different now as we no longer do new home construction as well as we do not do the snow clearing.
I want to focus on 2 things in particular on the website:

1/ Exterior renovations

2/ Detached Garage construction.

I have included our logo in the attached files to use as well.

Some features we would like:

1/ Be able to easily attach a video from Youtube/Vimeo to highlight a product or service
2/ Quick chat or contact button that we can talk to a potential client quickly
3/ Meet the Team page that is interesting and fresh
4/ Place for us to put in helpful exterior tips/suggestions for homeowners.

Content is not important, but looking for the best design that will attract people once they click on our page and want to renovate with us.

Target Market(s)

People looking for renovations on their home, people looking to build a detached garage.

Industry/Entity Type

Residential Construction

Coding

Coded - Design and coding required

Number of Pages Required

5+ page

Font styles to use
Sans Serif

Requirements
Must have
• Fresh and exciting home page.

Simple design. Don't want it over complicated or too much information to confuse the potential client.

Easy way to contact us.

Meet the team page that instills confidence
Nice to have
• Colour of website to go off our logo. Doesn't need to be an exact match, but something that goes well with our blue and grey.

```html
<!DOCTYPE html>
<html lang="en">
<head>
<meta charset="utf-8">
<title>Quellmark Exteriors</title>
<link href="https://fonts.googleapis.com/css2?family=Raleway:wght@500;600;700&family=Mulish:wght@400;600;700&display=swap" rel="stylesheet">
<style>
:root{
  --blue:#0a6fc2;
  --blue-dark:#0b4f8f;
  --ink:#333;
  --muted:#7a7a7a;
  --dark:#2a2a2a;
  --line:#cfcfcf;
  --white:#fff;
}
*{box-sizing:border-box;margin:0;padding:0}
html,body{width:1200px;height:4141px;overflow:hidden}
body{position:relative;font-family:'Mulish',sans-serif;color:var(--ink);background:var(--white)}
.abs{position:absolute}
.btn{position:absolute;background:var(--blue);color:var(--white);font:600 12px 'Mulish',sans-serif;text-transform:uppercase;display:flex;align-items:center;justify-content:center;letter-spacing:.3px}
.eyebrow{font:500 19px 'Raleway',sans-serif;text-transform:uppercase;color:#555}
.title{font:700 38px 'Raleway',sans-serif;text-transform:uppercase;color:#444}
.photo{position:absolute}
p.body{font-size:14px;line-height:22px;color:var(--muted)}

/* header */
.site-header{position:absolute;left:0;top:0;width:1200px;height:78px}
.brand{left:93px;top:22px}
.brand-name{font:700 24px 'Raleway',sans-serif;color:var(--blue)}
.header-phone{left:902px;top:16px;font-size:12px;color:#444;display:flex;align-items:center;gap:5px}
.nav{left:666px;top:53px;display:flex;font-size:11.5px;text-transform:uppercase}
.nav a{color:#444;text-decoration:none;width:104px}
.nav a.active{color:var(--blue)}

/* hero */
.hero{left:0;top:78px;width:1200px;height:522px;border-bottom-right-radius:90px;overflow:hidden;background:linear-gradient(180deg,#2f4a2c 0%,#5a6b44 35%,#6d5a3e 55%,#20303a 80%,#152028 100%)}
.hero-frame{left:522px;top:338px;width:143px;height:180px;border-top:5px solid var(--white);border-right:5px solid var(--white)}
.hero-frame2{left:671px;top:334px;width:150px;height:220px;border-top:5px solid var(--blue);border-left:5px solid var(--blue)}
.hero-copy{left:696px;top:352px;color:var(--white)}
.hero-copy .kicker{font:500 21px 'Raleway',sans-serif}
.hero-copy h1{font:700 41px/44px 'Raleway',sans-serif}
.hero-copy .lead{font-size:14px;margin-top:8px}
.slides{left:93px;top:558px;color:var(--white);font-size:10px}
.slides b{font-size:19px;margin:0 3px}

/* services */
.service-num{font-size:18px;color:#444}
.service-title{font:500 27px 'Raleway',sans-serif;color:#333}
.connector{height:1px;background:var(--line)}

/* video */
.video-band{left:0;top:1461px;width:1200px;height:359px;background:linear-gradient(180deg,#0d4f86,#0a5f9f 60%,#0b6cb5)}
.video-head{left:0;width:1200px;text-align:center;color:var(--white)}
.video-box{left:271px;top:1600px;width:656px;height:380px;background:linear-gradient(180deg,#8a6d4c,#c9b995 45%,#9a8a6a 100%)}
.player-bar{left:22px;top:325px;width:610px;height:40px;display:flex;align-items:center;gap:14px}
.play{width:66px;height:40px;background:rgba(0,0,0,.8);display:flex;align-items:center;justify-content:center}
.track{flex:1;height:12px;background:rgba(0,0,0,.7);position:relative;border:1px solid #111}
.track i{position:absolute;left:2px;top:2px;width:10px;height:6px;background:#2aa7e8}
.side-tools{right:24px;top:50px;display:flex;flex-direction:column;gap:8px}
.side-tools span{width:40px;height:38px;background:rgba(0,0,0,.8);color:var(--white);font-size:8px;font-weight:700;display:flex;align-items:flex-end;justify-content:center;padding-bottom:4px}

/* team */
.center{left:0;width:1200px;text-align:center}
.member{position:absolute;top:2179px;width:230px;text-align:center}
.member .shelf{position:absolute;left:0;top:0;width:230px;height:18px;background:#e6e6e6;clip-path:polygon(6% 0,94% 0,100% 100%,0 100%)}
.member .ring{position:relative;margin:0 auto;width:172px;height:172px;border-radius:50%;border:7px solid var(--blue);background:var(--white);padding:7px}
.member .ring div{width:100%;height:100%;border-radius:50%;background:linear-gradient(180deg,#a9b9a0,#8a8a5a 55%,#5c6a3c)}
.member h3{font:500 18px 'Raleway',sans-serif;color:var(--blue);margin-top:18px}
.member small{font-size:11.5px;color:#555;display:block}
.member .btn{left:68px;top:240px;width:106px;height:32px;position:absolute}

/* about */
.about{left:0;top:2518px;width:1200px;height:434px;background:var(--dark);overflow:hidden}
.about .eyebrow{color:var(--white)}
.about .title{color:var(--white)}
.about p.body{color:#c9c9c9}
.gallery-cell{position:absolute;top:0;height:434px;width:207px}
.gallery-label{position:absolute;color:var(--white);font-size:10px;width:207px;text-align:center}

/* contact */
.field{position:absolute;border:1px solid var(--line);font-size:11px;color:#777;padding:10px 14px;height:36px}

/* projects */
.projects{left:0;top:3332px;width:1200px;height:523px;background:linear-gradient(180deg,#0b5aa6,#0a6fc2 50%,#0a4f94)}
.projects-panel{left:389px;top:3496px;width:424px;height:306px;background:rgba(7,55,105,.55)}
.thumb{position:absolute;top:3520px;width:193px;height:195px}
.arrow-dot{position:absolute;top:3761px;width:26px;height:26px;border-radius:50%;border:1px solid rgba(255,255,255,.6);color:var(--white);font-size:12px;display:flex;align-items:center;justify-content:center}

/* footer */
.footer{left:0;top:3855px;width:1200px;height:286px;background:var(--dark);border-bottom-left-radius:60px;color:#ccc}
.footer h4{font:500 18px 'Raleway',sans-serif;color:var(--white)}
.footer ul{list-style:none;font-size:11.5px;line-height:21.5px;margin-top:10px}
.footer .col{position:absolute;top:59px}
.footer .info{font-size:11.5px;display:flex;align-items:center;gap:6px}
.socials{display:flex;gap:5px;margin-top:6px}
.socials span{width:21px;height:21px;border-radius:50%;background:var(--white)}
.copyright{left:0;top:226px;width:1200px;text-align:center;font-size:11px;color:#aaa}
.copyright b{color:var(--white);font-weight:400}
.quick-float{left:1012px;top:4117px;width:94px;height:28px;background:#f5a623;border-radius:8px 8px 0 0;color:var(--white);font-size:11px;display:flex;align-items:center;justify-content:center;text-transform:uppercase}
</style>
</head>
<body>

<header class="site-header">
  <div class="abs brand"><span class="brand-name">Quellmark Exteriors</span></div>
  <div class="abs header-phone">
    <svg width="10" height="12" viewBox="0 0 10 12"><path d="M2 0l2 3-1.3 1.3c.5 1.5 1.6 2.7 3 3.4L7 6.4l3 2-1 2.6C4 11 0 6 1 1z" fill="#0a6fc2"/></svg>780-555-0147</div>
  <div class="btn" style="left:1002px;top:7px;width:105px;height:34px">Quick Chat</div>
  <nav class="abs nav">
    <a class="active">Home</a><a>Services</a><a>Projects</a><a style="width:80px">Team</a><a>Contact Us</a>
  </nav>
</header>

<section class="abs hero" role="img" aria-label="Wooden lake house with a stone porch reflected in still water, forest behind"></section>
<div class="abs hero-frame"></div>
<div class="abs hero-frame2"></div>
<div class="abs hero-copy">
  <div class="kicker">Honest and</div>
  <h1>Reliable<br>Construction Service</h1>
  <div class="lead">We take pride in each and every project</div>
</div>
<div class="btn" style="left:697px;top:513px;width:111px;height:32px">Get a Qoute</div>
<div class="abs slides">01 <b>02</b> 03</div>

<div class="abs eyebrow" style="left:93px;top:660px">What we do</div>
<h2 class="abs title" style="left:93px;top:690px">Our Services</h2>

<div class="photo" role="img" aria-label="House under renovation with roof framing against a blue sky" style="left:93px;top:747px;width:506px;height:310px;background:linear-gradient(180deg,#3f84d0 0%,#9cc3ea 45%,#a3826a 70%,#5b7a3a 100%)"></div>
<div class="abs connector" style="left:602px;top:789px;width:50px"></div>
<div class="abs service-num" style="left:666px;top:779px">01</div>
<h3 class="abs service-title" style="left:665px;top:823px">Exterior Renovations</h3>
<p class="abs body" style="left:665px;top:866px;width:440px">Looking for a reputable company to replace those aging shingles? Wanting to update the look of your home to add more curb appeal? We can handle all your exterior renovation needs and would love an opportunity to speak with you about it. Contact us for a free, no obligation quote today.</p>
<div class="btn" style="left:665px;top:988px;width:105px;height:32px">Read More</div>

<div class="abs service-num" style="left:511px;top:1118px">02</div>
<div class="abs connector" style="left:548px;top:1128px;width:50px"></div>
<h3 class="abs service-title" style="left:93px;top:1162px;width:441px;text-align:right">Detached Garage construction</h3>
<p class="abs body" style="left:93px;top:1205px;width:441px;text-align:right">Sed ut perspiciatis unde omnis iste natus error sit voluptatem accusantium doloremque laudantium, totam rem aperiam, eaque ipsa quae ab illo inventore veritatis et quasi architecto beatae vitae dicta sunt explicabo. Nemo enim ipsam voluptatem quia voluptas sit aspernatur aut odit aut fugit</p>
<div class="btn" style="left:429px;top:1327px;width:105px;height:32px">Read More</div>
<div class="photo" role="img" aria-label="Garage frame model with white walls and steel roof trusses on grass" style="left:601px;top:1084px;width:506px;height:310px;background:linear-gradient(160deg,#3a5d2a 0%,#7f9a5b 40%,#dfe2e4 55%,#a9adb1 75%,#6a8a44 100%)"></div>

<section class="abs video-band" role="img" aria-label="Blue tinted landscape with lake and hills"></section>
<div class="abs video-head eyebrow" style="top:1504px;color:#fff">What Video</div>
<h2 class="abs video-head title" style="top:1532px;color:#fff">Quellmark Exteriors</h2>
<div class="abs video-box" role="img" aria-label="Video still of workers installing siding on a house wall">
  <div class="abs side-tools"><span>LIKE</span><span>LATER</span><span>SHARE</span><span>EMBED</span></div>
  <div class="abs player-bar">
    <div class="play"><svg width="16" height="18"><rect x="1" y="0" width="5" height="18" fill="#fff"/><rect x="10" y="0" width="5" height="18" fill="#fff"/></svg></div>
    <div class="track"><i></i></div>
    <span style="color:#2aa7e8;font:700 14px 'Mulish',sans-serif">HD</span>
  </div>
</div>

<div class="abs center eyebrow" style="top:2043px">Experienced</div>
<h2 class="abs center title" style="top:2072px">Our Team</h2>
<p class="abs center" style="top:2124px;font-size:13.5px;color:#666">Sed ut perspiciatis unde omnis iste natus error sit voluptatem accusantium</p>

<div class="member" style="left:106px"><span class="shelf"></span><div class="ring"><div role="img" aria-label="Portrait of team member in a field"></div></div><h3>Devin Ashcroft</h3><small>General Manager</small><div class="btn">View Details</div></div>
<div class="member" style="left:359px"><span class="shelf"></span><div class="ring"><div role="img" aria-label="Portrait of team member in a field"></div></div><h3>Colby Varnum</h3><small>Operations Manager (Exteriors)</small><div class="btn">View Details</div></div>
<div class="member" style="left:612px"><span class="shelf"></span><div class="ring"><div role="img" aria-label="Portrait of team member in a field"></div></div><h3>Elias Brandvold</h3><small>Field Service Manager</small><div class="btn">View Details</div></div>
<div class="member" style="left:866px"><span class="shelf"></span><div class="ring"><div role="img" aria-label="Portrait of team member in a field"></div></div><h3>Marisa Quenneville</h3><small>Administrative Assistant</small><div class="btn">View Details</div></div>

<section class="abs about">
  <div class="abs eyebrow" style="left:95px;top:100px">We help you</div>
  <h2 class="abs title" style="left:95px;top:128px">About Exteriors</h2>
  <p class="abs body" style="left:93px;top:182px;width:420px">Sed ut perspiciatis unde omnis iste natus error sit voluptatem accusantium doloremque laudantium, totam rem aperiam, eaque ipsa quae ab illo inventore veritatis et quasi architecto beatae vitae dicta sunt explicabo. Nemo enim ipsam voluptatem quia voluptas sit aspernatur aut odit aut fugit.</p>
  <div class="btn" style="left:93px;top:303px;width:105px;height:32px">Contact Us</div>
  <div class="gallery-cell" role="img" aria-label="White siding house gable against blue sky" style="left:580px;top:30px;height:404px;background:linear-gradient(180deg,#6fa3d8,#dfe6ee 50%,#b7bfc6)"></div>
  <div class="gallery-label" style="left:580px;top:9px">01</div>
  <div class="gallery-cell" role="img" aria-label="Two storey home overlooking a lake and trees" style="left:787px;height:404px;background:linear-gradient(180deg,#5b7c5a,#8c9a6a 45%,#6a6042 75%,#3f5a2e)"></div>
  <div class="gallery-label" style="left:787px;top:414px">02</div>
  <div class="gallery-cell" role="img" aria-label="Stone house with a garage at dusk" style="left:994px;top:30px;height:404px;width:206px;background:linear-gradient(180deg,#8aa5c2,#b8967a 45%,#8c6a50 75%,#5a7a3a)"></div>
  <div class="gallery-label" style="left:994px;top:9px;width:206px">03</div>
</section>

<div class="photo" role="img" aria-label="Model of a modern house with a white garage" style="left:64px;top:3019px;width:386px;height:249px;background:radial-gradient(ellipse at 55% 55%,#9a8a70 0%,#d9d6d0 45%,#fff 75%)"></div>
<div class="abs eyebrow" style="left:482px;top:3016px">Get in touch</div>
<h2 class="abs title" style="left:482px;top:3045px">Contact Us</h2>
<div class="field" style="left:482px;top:3105px;width:311px">Name:</div>
<div class="field" style="left:482px;top:3147px;width:311px">Email:</div>
<div class="field" style="left:482px;top:3189px;width:311px">Phone:</div>
<div class="field" style="left:482px;top:3231px;width:311px">Services:</div>
<div class="field" style="left:797px;top:3105px;width:311px;height:120px">Comments:</div>
<div class="btn" style="left:797px;top:3231px;width:311px;height:36px">Submit</div>

<section class="abs projects"></section>
<div class="abs projects-panel"></div>
<div class="abs center eyebrow" style="top:3378px;color:#fff">Portfolio</div>
<h2 class="abs center title" style="top:3408px;color:#fff">Past Projects</h2>
<div class="thumb" role="img" aria-label="Dark modern house exterior" style="left:93px;background:linear-gradient(180deg,#555,#2a2a2a)"></div>
<div class="thumb" role="img" aria-label="Bright kitchen with island" style="left:299px;background:linear-gradient(180deg,#e6e2dc,#a9a29a)"></div>
<div class="thumb" role="img" aria-label="New custom home under construction" style="left:504px;background:linear-gradient(180deg,#c8c8c8,#8a7a6a 60%,#6a6a5a)"></div>
<div class="thumb" role="img" aria-label="Modern home lit at dusk" style="left:710px;background:linear-gradient(180deg,#5a88c0,#c89060 60%,#6a4a2a)"></div>
<div class="thumb" role="img" aria-label="Dark exterior staircase" style="left:914px;background:linear-gradient(180deg,#4a4a4a,#1f1f1f)"></div>
<div class="abs center" style="top:3730px;color:#fff;font-size:11px">Current</div>
<div class="abs center" style="top:3743px;color:#fff;font-size:15px">Custom Home Build</div>
<div class="arrow-dot" style="left:369px">&lsaquo;</div>
<div class="arrow-dot" style="left:807px">&rsaquo;</div>

<footer class="abs footer">
  <div class="col" style="left:93px"><h4>Company</h4><ul><li>Home</li><li>About Us</li><li>Services</li><li>Team</li><li>Contact Us</li></ul></div>
  <div class="col" style="left:260px"><h4>Help Center</h4><ul><li>FAQ's</li><li>Terms &amp; Condition</li><li>Privacy</li><li>How It Work</li><li>Help</li></ul></div>
  <div class="col" style="left:429px"><h4>Office Hours</h4><ul><li>Mon-Fri: 8:00-4:30</li><li>Sat-Sun &amp; Holidays: Closed</li></ul>
    <div style="font-size:11.5px;color:#fff;margin-top:28px">Follow Us</div>
    <div class="socials"><span></span><span></span><span></span></div></div>
  <div class="col" style="left:644px"><h4>Get In Touch</h4>
    <div class="info" style="margin-top:12px"><svg width="9" height="12" viewBox="0 0 9 12"><path d="M4.5 0A4.5 4.5 0 0 0 0 4.5C0 8 4.5 12 4.5 12S9 8 9 4.5A4.5 4.5 0 0 0 4.5 0zm0 6.3a1.8 1.8 0 1 1 0-3.6 1.8 1.8 0 0 1 0 3.6z" fill="#fff"/></svg>Harlow Park, Alberta</div>
    <div class="info" style="margin-top:16px"><svg width="11" height="8"><rect width="11" height="8" fill="#fff"/><path d="M0 0l5.5 4L11 0" stroke="#2a2a2a" fill="none"/></svg>info@quellmarkbuilders.ca</div>
    <div class="info" style="margin-top:16px"><svg width="10" height="12" viewBox="0 0 10 12"><path d="M2 0l2 3-1.3 1.3c.5 1.5 1.6 2.7 3 3.4L7 6.4l3 2-1 2.6C4 11 0 6 1 1z" fill="#fff"/></svg>780-555-0147</div></div>
  <div class="col" style="left:846px;width:261px"><h4>Newsletter</h4>
    <p style="font-size:11px;line-height:16px;margin-top:12px">If you use this site regularly and would like to help</p>
    <div style="margin-top:10px;background:#fff;height:28px;font-size:10.5px;color:#666;padding:7px 10px">Enter Your Email:</div>
    <div class="btn" style="position:relative;margin-top:6px;height:30px">Subscribe</div></div>
  <div class="abs copyright">Copyright &copy; 2020 <b>Quellmark Exteriors</b>. All rights reserved.</div>
</footer>
<div class="abs quick-float">Quick Chat</div>

</body>
</html>
```